Business Card design for new private practice opening

I need a business card design for my new private practice with my new logo uploaded as a file
On the front the logo
On the back: maybe a small logo somewhere?
Priv. Doz. DDr. Corinna Vestaluk
Fachärztin für Allgemein- & Viszeralchirurgie
Address: xxx
Tel: xxx
Mobil:xxx
Webseite:xxx
Email:xxx

Contact Information for Business Card

See project description above for details

Requirements
Nice to have
• I would like the colors of the logo incorporated into the business card

```html
<!DOCTYPE html>
<html lang="de">
<head>
<meta charset="utf-8">
<title>Vestaluk Chirurgie – Visitenkarte</title>
<link rel="stylesheet" href="https://fonts.googleapis.com/css2?family=Montserrat:ital,wght@0,500;0,600;1,500;1,600&display=swap">
<style>
  :root {
    --teal: #3dbcb6;
    --grey: #8a8a8a;
    --paper: #ffffff;
    --stage: #ffffff;
    --shadow: rgba(0, 0, 0, 0.35);
  }
  * { margin: 0; padding: 0; box-sizing: border-box; }
  html, body {
    width: 1200px; height: 1200px; overflow: hidden;
    background: var(--stage);
    font-family: "Montserrat", Arial, sans-serif;
  }
  .canvas { position: relative; width: 1200px; height: 1200px; }
  .card {
    position: absolute; left: 272px; width: 655px; height: 414px;
    background: var(--paper);
    box-shadow: 4px 5px 6px var(--shadow);
    overflow: hidden;
  }
  .card--front { top: 147px; }
  .card--back { top: 644px; }

  .front-band {
    position: absolute; left: 0; right: 0; bottom: 0; height: 12px;
    background: var(--teal);
  }
  .brand-mark {
    position: absolute; border-radius: 50%;
    background: var(--teal); border: 4px solid var(--grey);
  }
  .card--front .brand-mark { left: 113px; top: 136px; width: 128px; height: 128px; }
  .brand-name {
    position: absolute; color: var(--grey); font-weight: 600;
    text-transform: uppercase; line-height: 1;
  }
  .card--front .brand-name {
    left: 258px; top: 156px; font-size: 52px; line-height: 53px; letter-spacing: 0.5px;
  }

  .doctor {
    position: absolute; left: 0; right: 0; top: 44px; text-align: center; color: var(--grey);
  }
  .doctor-name { font-size: 26px; font-weight: 600; letter-spacing: 0.2px; }
  .doctor-title { font-style: italic; font-weight: 500; }
  .doctor-specialty { font-size: 21px; font-style: italic; font-weight: 600; margin-top: 2px; }

  .contact-icons {
    position: absolute; left: 33px; top: 238px; list-style: none;
    display: flex; flex-direction: column; gap: 3px;
  }
  .contact-icons li {
    width: 28px; height: 28px; border-radius: 50%; background: var(--teal);
    display: flex; align-items: center; justify-content: center;
  }
  .contact-icons svg { width: 16px; height: 16px; }

  .card--back .brand-mark { left: 511px; top: 269px; width: 112px; height: 112px; }
  .card--back .brand-name {
    right: 160px; top: 304px; font-size: 18px; line-height: 22px; text-align: right;
  }
</style>
</head>
<body>
<main class="canvas">
  <section class="card card--front" aria-label="Vorderseite">
    <div class="brand-mark"></div>
    <div class="brand-name">Vestaluk<br>Chirurgie</div>
    <div class="front-band"></div>
  </section>

  <section class="card card--back" aria-label="Rückseite">
    <div class="doctor">
      <p class="doctor-name"><span class="doctor-title">Priv. Doz. DDr.</span> CORINNA VESTALUK</p>
      <p class="doctor-specialty">Specialist in General &amp; Visceral Surgery</p>
    </div>

    <ul class="contact-icons">
      <li aria-label="Telefon">
        <svg viewBox="0 0 24 24" fill="none" stroke="#fff" stroke-width="2" stroke-linecap="round" stroke-linejoin="round"><path d="M5 3h3l2 5-2 1.5a11 11 0 0 0 6.5 6.5L16 14l5 2v3a2 2 0 0 1-2 2A16 16 0 0 1 3 5a2 2 0 0 1 2-2z"/><path d="M14 3a7 7 0 0 1 7 7M14 7a3 3 0 0 1 3 3"/></svg>
      </li>
      <li aria-label="Mobil">
        <svg viewBox="0 0 24 24" fill="none" stroke="#fff" stroke-width="2" stroke-linecap="round"><rect x="7" y="2" width="10" height="20" rx="2"/><path d="M11 18h2"/></svg>
      </li>
      <li aria-label="E-Mail">
        <svg viewBox="0 0 24 24" fill="none" stroke="#fff" stroke-width="2" stroke-linejoin="round"><rect x="3" y="6" width="18" height="13"/><path d="M3 6l9 7 9-7"/></svg>
      </li>
      <li aria-label="Adresse">
        <svg viewBox="0 0 24 24"><path fill="#fff" d="M12 2a7 7 0 0 0-7 7c0 5 7 13 7 13s7-8 7-13a7 7 0 0 0-7-7zm0 9.5A2.5 2.5 0 1 1 12 6.5a2.5 2.5 0 0 1 0 5z"/></svg>
      </li>
      <li aria-label="Webseite">
        <svg viewBox="0 0 24 24" fill="none" stroke="#fff" stroke-width="1.6"><circle cx="12" cy="12" r="9"/><ellipse cx="12" cy="12" rx="4" ry="9"/><path d="M3 12h18M5 7h14M5 17h14"/></svg>
      </li>
    </ul>

    <div class="brand-name">Vestaluk<br>Chirurgie</div>
    <div class="brand-mark"></div>
  </section>
</main>
</body>
</html>
```